Brolvane Co.,Ltd. need business card

Brolvane Company Limited is a facility management company. We provides a total solution services from administration, energy saving, security, safety, food catering to companies.

The logo should be in elegant style with innovative that suited to the upper market
Please see the logo image in the attached file. You can use this Red or Blue or Green checkerboard (color and font should be similar to logo) as the main part of business card (can be an entire of one side of business card) . In another side of card should contain contact details of personnel - here below demo information

Kanyarat Thoengsai
Chief Executive Officer

No.73, Soi 5, Ruam Wongsa Road
Nong Khaem, Bangkok,
10520, Thailand

Tel + 66841537296
Mobile + 66841537296
E-mail: Kanyarat.Thoengsai@brolvane-example.co.th

Target Market(s)

Factory, Hotel and Hospital

Industry/Entity Type

Business

Contact Information for Business Card

Kanyarat Thoengsai
Chief Executive Officer

Nong Khaem, Bangkok,
10520, Thailand

Tel + 66841537296
Mobile + 66841537296

We will change details with the winner designer

Font styles to use
Sans Serif

Requirements
Must have
• In style of red checkerboard and white color

```html
<!DOCTYPE html>
<html lang="en">
<head>
<meta charset="utf-8">
<title>Brolvane Co.,Ltd. – Business Card</title>
<link href="https://fonts.googleapis.com/css2?family=Open+Sans:wght@300;400;600;700&display=swap" rel="stylesheet">
<style>
  :root {
    --bg: #e9e4dc;
    --red-deep: #a81f27;
    --red-mid: #bd2b32;
    --red-light: #cc3a3e;
    --white: #ffffff;
    --white-soft: rgba(255,255,255,0.85);
  }
  * { margin: 0; padding: 0; box-sizing: border-box; }
  html, body {
    width: 1200px; height: 780px; overflow: hidden;
    background: var(--bg);
    font-family: "Open Sans", Arial, sans-serif;
  }
  .canvas {
    position: relative; width: 1200px; height: 780px;
  }
  .card {
    position: absolute; top: 235px;
    width: 540px; height: 310px;
    border-radius: 18px;
    overflow: hidden;
    color: var(--white);
    box-shadow: 0 4px 0 var(--red-deep), 0 12px 24px rgba(0,0,0,0.18);
  }
  .card--front {
    left: 40px;
    background: linear-gradient(135deg, var(--red-mid) 0%, var(--red-light) 55%, var(--red-mid) 100%);
  }
  .card--back { left: 620px; }

  /* front */
  .front-brand {
    position: absolute; left: 34px; top: 118px;
    font-weight: 300; font-size: 44px; letter-spacing: 6px;
    color: var(--white);
  }
  .person { position: absolute; right: 34px; top: 46px; text-align: right; }
  .person__name { font-weight: 700; font-size: 17px; letter-spacing: 0.3px; }
  .person__title { font-weight: 400; font-size: 13px; margin-top: 1px; }
  .divider {
    position: absolute; left: 150px; right: 34px; top: 112px;
    height: 1px; background: var(--white-soft);
  }
  .address {
    position: absolute; right: 34px; top: 132px; text-align: right;
    font-size: 12.5px; line-height: 1.45;
  }
  .contacts {
    position: absolute; left: 34px; bottom: 30px;
    list-style: none; font-size: 12.5px; line-height: 1.5;
  }
  .contacts li { display: flex; align-items: center; gap: 7px; margin-top: 3px; }
  .contacts svg { width: 16px; height: 16px; flex: none; }

  /* back */
  .back-texture {
    position: absolute; inset: 0;
    background: linear-gradient(135deg, var(--red-deep) 0%, var(--red-mid) 50%, var(--red-light) 100%);
  }
  .back-content {
    position: absolute; inset: 0;
    display: flex; flex-direction: column; align-items: center; justify-content: center;
  }
  .back-brand {
    font-weight: 300; font-size: 58px; letter-spacing: 8px;
  }
  .back-services {
    font-weight: 600; font-size: 15px; letter-spacing: 0.5px; margin-top: 8px;
  }
  .back-tagline {
    font-weight: 400; font-size: 13px; margin-top: 6px;
  }
</style>
</head>
<body>
<main class="canvas">

  <section class="card card--front" aria-label="Business card front">
    <div class="front-brand">BROLVANE</div>

    <div class="person">
      <div class="person__name">KANYARAT THOENGSAI</div>
      <div class="person__title">Chief Executive Officer</div>
    </div>

    <div class="divider"></div>

    <address class="address" style="font-style:normal">
      No.73, Soi 5, Ruam Wongsa Road<br>
      Nong Khaem, Bangkok<br>
      10520, Thailand
    </address>

    <ul class="contacts">
      <li>
        <svg viewBox="0 0 16 16" aria-hidden="true"><rect width="16" height="16" rx="3" fill="#fff"/><path d="M4 5.5c0-.8.6-1.5 1.5-1.5h5c.9 0 1.5.7 1.5 1.5v.5H9.5V5h-3v1H4z M5 7h6l1 4.5H4z" fill="#bd2b32"/></svg>
        + 66841537296
      </li>
      <li>
        <svg viewBox="0 0 16 16" aria-hidden="true"><rect width="16" height="16" rx="3" fill="#fff"/><rect x="5" y="2.5" width="6" height="11" rx="1" fill="#bd2b32"/><rect x="6" y="4" width="4" height="6" fill="#fff"/></svg>
        + 66841537296
      </li>
      <li>
        <svg viewBox="0 0 16 16" aria-hidden="true"><rect width="16" height="16" rx="3" fill="#fff"/><rect x="3" y="4.5" width="10" height="7" fill="none" stroke="#bd2b32" stroke-width="1.3"/><path d="M3 4.5l5 4 5-4" fill="none" stroke="#bd2b32" stroke-width="1.3"/></svg>
        Kanyarat.Thoengsai@brolvane-example.co.th
      </li>
    </ul>
  </section>

  <section class="card card--back" aria-label="Business card back">
    <div class="back-texture" role="img" aria-label="Subtle red checkerboard pattern background"></div>
    <div class="back-content">
      <div class="back-brand">BROLVANE</div>
      <div class="back-services">SERVICES</div>
      <div class="back-tagline">energy saving, security, safety, food catering to companies.</div>
    </div>
  </section>

</main>
</body>
</html>
```